Craft Flavoured Beer Family Extension Desing

We are a Canadian craft brewery looking for the design of a new line of beer we wish to launch within an existing family of products. Our beers are high craft beers that retail for a significant price. Example, 4.49$ for 500 mL vs. 1.49$ for a 500 mL Valdermost.

The line of beer that is being designed here is for a craft flavoured beer line targeted to women. This will be light tasting beers with light fruit flavors targeted to consumers who like beer but are not ready for the strong IPA which are generally found in the craft beer offerings.

The Marisette line, which is the name of this new product, is a ''cousin'' of the existing Gaston-Ferrand Line (more info below).

Target Market(s)

60% Females 40% Males - 21 to 40 years old

Industry/Entity Type

Brewery

Requirements
Must have
• The products will be an INDIRECT family/line extension of the Gaston-Ferrand line of products (design attached). There needs to be some similarities, but it cannot be too close. There are 3 main features on the Gaston-Ferrand label (attached) : (1) the font used for the Logo; (2) the shape of the label; (3) the motif printed on the label.
• The shape of the label must be different than the current shape.
• However, the font of the logo (Gaston-Ferrand) can be the same and the motif printed on the label can be used. Using one of these elements is sufficient to link this new brand with the Gaston-Ferrand brand.
• The name of the product will be MARISETTE
Nice to have
• The bottle, the size, the ABV will be different than for the Gaston-Ferrand beers.
• There will be 3 flavours initially : Blueberry, Grapefruit and Raspberry.
• There needs to be a back label, but if you design, you can use the exact same information as there is currently.
Should not have
• We don't want any fruit pictures or designs on the labels.

```html
<!DOCTYPE html>
<html lang="en">
<head>
<meta charset="utf-8">
<title>Marisette Raspberry Label</title>
<link rel="stylesheet" href="https://fonts.googleapis.com/css2?family=Great+Vibes&family=Libre+Baskerville:wght@400;700&family=Playfair+Display:wght@700&display=swap">
<style>
  :root {
    --maroon: #8c1a2e;
    --maroon-dark: #6e1222;
    --cream: #fbf3c4;
    --ink: #1c1414;
    --gold: #c9a24a;
    --page: #ffffff;
  }
  html, body {
    margin: 0;
    padding: 0;
    width: 773px;
    height: 1200px;
    overflow: hidden;
    background: var(--page);
  }
  .canvas {
    position: relative;
    width: 773px;
    height: 1200px;
  }
  .label {
    position: absolute;
    left: 66px;
    top: 170px;
    width: 640px;
    height: 862px;
  }
  .label-shape {
    position: absolute;
    inset: 0;
  }
  .label-text {
    position: absolute;
    left: 0;
    width: 640px;
    text-align: center;
    margin: 0;
  }
  .ornament {
    position: absolute;
    left: 50%;
    transform: translateX(-50%);
    border-radius: 50% 50% 12px 12px;
    background: linear-gradient(180deg, #b4495a, var(--maroon));
  }
  .ornament-top {
    top: 52px;
    width: 220px;
    height: 92px;
  }
  .ornament-bottom {
    top: 700px;
    width: 170px;
    height: 48px;
    border-radius: 12px 12px 50% 50%;
  }
  .brewery {
    top: 162px;
    font-family: "Libre Baskerville", serif;
    font-size: 30px;
    line-height: 36px;
    letter-spacing: 1px;
    color: var(--maroon);
  }
  .product-name {
    top: 232px;
    font-family: "Great Vibes", cursive;
    font-size: 112px;
    line-height: 112px;
    font-weight: 400;
    color: var(--ink);
  }
  .flavour-band {
    position: absolute;
    left: 22px;
    top: 400px;
    width: 596px;
    height: 70px;
    background: var(--maroon);
    display: flex;
    align-items: center;
    justify-content: center;
  }
  .flavour {
    font-family: "Playfair Display", serif;
    font-size: 46px;
    letter-spacing: 10px;
    color: var(--cream);
    margin: 0;
  }
  .origin {
    top: 500px;
    font-family: "Libre Baskerville", serif;
    font-size: 32px;
    letter-spacing: 2px;
    color: var(--maroon);
  }
  .rule {
    position: absolute;
    left: 70px;
    width: 500px;
    height: 3px;
    background: var(--maroon);
  }
  .rule-upper { top: 560px; }
  .rule-lower { top: 672px; }
  .facts {
    position: absolute;
    left: 70px;
    top: 580px;
    width: 500px;
    height: 80px;
    display: flex;
    align-items: center;
    justify-content: space-between;
    font-family: "Libre Baskerville", serif;
    color: var(--maroon);
  }
  .fact-type {
    font-size: 22px;
    line-height: 1.3;
    text-align: left;
  }
  .fact-volume {
    font-size: 58px;
    color: var(--ink);
  }
  .fact-abv {
    font-size: 22px;
    line-height: 1.3;
    text-align: center;
  }
  .fact-abv small {
    font-size: 16px;
  }
</style>
</head>
<body>
<main class="canvas">
  <section class="label">
    <svg class="label-shape" width="640" height="862" viewBox="0 0 640 862" aria-hidden="true">
      <polygon points="0,0 640,0 640,730 320,862 0,730" fill="var(--maroon)"/>
      <polygon points="12,12 628,12 628,722 320,849 12,722" fill="var(--cream)"/>
      <polygon points="24,24 616,24 616,714 320,836 24,714" fill="none" stroke="var(--maroon)" stroke-width="3"/>
      <line x1="160" y1="372" x2="480" y2="372" stroke="var(--maroon)" stroke-width="3" stroke-linecap="round"/>
      <circle cx="320" cy="372" r="6" fill="var(--maroon)"/>
    </svg>

    <div class="ornament ornament-top" role="img" aria-label="Decorative crest ornament"></div>

    <p class="label-text brewery">BRASSERIE DU VIEUX PONT</p>
    <h1 class="label-text product-name">Marisette</h1>

    <div class="flavour-band">
      <p class="flavour">RASBERRY</p>
    </div>

    <p class="label-text origin">BRASSEE AU QUEBEC</p>

    <div class="rule rule-upper"></div>
    <div class="facts">
      <div class="fact-type">BIERRE<br>BEER</div>
      <div class="fact-volume">500 mL.</div>
      <div class="fact-abv">5%<br><small>alc/vol.</small></div>
    </div>
    <div class="rule rule-lower"></div>

    <div class="ornament ornament-bottom" role="img" aria-label="Decorative scroll ornament"></div>
  </section>
</main>
</body>
</html>
```